Decorative concrete business needs new business cards

Our company attracts homeowners and business with disposable cash. We are a artistic decorative coatings company that will transform your driveway, patio, floors or counter tops into a work of art. We also engrave logos and designs right into the concrete! We are upscale and very professional company. I am open for rearranging our logo on the business card and also to different color patterns. We like the blue and black as in BrushNest's logo. We also like blue and orange/yellow.

Target Market(s)

Adults 30-70

Industry/Entity Type

Concrete

Contact Information for Business Card

Simple: Name, phone, email, website and social media icons

Font styles to use
Serif

Colors

Designer to choose colors to be used in the design.

Requirements
Must have
• Must present a professional upscale appearance. I have attached before and after photos that show you what our industry does. Maybe I will have before and after photo on back of card.
Nice to have
• Artistic, but bold. Nothing whimsical or cute.
Should not have
• Should not have cartoon or childlike appearance.

```html
<!DOCTYPE html>
<html lang="en">
<head>
<meta charset="utf-8">
<title>Crestline Surface Finishes – Business Card</title>
<link rel="stylesheet" href="https://fonts.googleapis.com/css2?family=Cinzel:wght@500&family=Open+Sans:wght@400&display=swap">
<style>
  :root {
    --page-bg: #e9e7e4;
    --card-white: #ffffff;
    --brand-blue: #1a73b8;
    --ink: #222222;
    --text: #2b2b2b;
    --faint-blue: #edf1f7;
    --label-bg: #262626;
    --white: #ffffff;
    --before-tone: #9a9892;
    --after-tone: #7a6548;
  }
  * { box-sizing: border-box; margin: 0; padding: 0; }
  html, body { width: 1200px; height: 1000px; overflow: hidden; }
  body { background: var(--page-bg); position: relative; font-family: "Open Sans", Arial, sans-serif; color: var(--text); }

  .card { position: absolute; left: 266px; width: 666px; height: 397px; overflow: hidden; box-shadow: 0 4px 12px rgba(0,0,0,.18); }
  .card-front { top: 74px; background: var(--card-white); }
  .card-back { top: 533px; }

  .holder-name { position: absolute; left: 33px; top: 64px; font-family: "Cinzel", Georgia, serif; font-weight: 500; font-size: 23px; color: var(--brand-blue); letter-spacing: .5px; }
  .holder-role { position: absolute; left: 33px; top: 93px; font-size: 16px; }
  .address { position: absolute; left: 33px; top: 186px; font-size: 16px; line-height: 25px; }
  .contact-list { position: absolute; left: 33px; top: 255px; list-style: none; font-size: 16px; line-height: 25px; }
  .contact-list li { display: flex; align-items: center; gap: 6px; }
  .contact-list svg { width: 15px; height: 15px; fill: var(--brand-blue); }
  .social { position: absolute; left: 33px; top: 342px; display: flex; align-items: center; gap: 6px; font-size: 16px; }
  .social-dot { width: 18px; height: 18px; border-radius: 50%; background: var(--brand-blue); }
  .social-handle { margin-left: 4px; }

  .brand-lockup { position: absolute; display: flex; align-items: center; gap: 12px; font-family: "Cinzel", Georgia, serif; font-weight: 500; line-height: 1; }
  .brand-front { left: 355px; top: 46px; color: var(--brand-blue); }
  .brand-front .brand-mark { width: 78px; height: 78px; background: var(--ink); }
  .brand-name span { display: block; white-space: nowrap; }
  .brand-front .line-1 { font-size: 30px; }
  .brand-front .line-2 { font-size: 24px; margin-top: 2px; }
  .brand-front .line-3 { font-size: 19px; letter-spacing: 4px; margin-top: 2px; }
  .faint-block { position: absolute; left: 355px; top: 160px; width: 278px; height: 240px; background: var(--faint-blue); }

  .surface-photo { position: absolute; inset: 0; background: linear-gradient(90deg, var(--before-tone) 0%, var(--before-tone) 50%, var(--after-tone) 50%, var(--after-tone) 100%); }
  .surface-photo::after { content: ""; position: absolute; inset: 0; background: linear-gradient(180deg, rgba(60,50,40,.55) 0%, rgba(60,50,40,.15) 45%, rgba(0,0,0,0) 60%); }
  .brand-back { left: 178px; top: 86px; color: var(--white); gap: 14px; }
  .brand-back .brand-mark { width: 86px; height: 86px; background: var(--white); }
  .brand-back .line-1 { font-size: 36px; }
  .brand-back .line-2 { font-size: 28px; margin-top: 2px; }
  .brand-back .line-3 { font-size: 22px; letter-spacing: 5px; margin-top: 2px; }

  .compare-label { position: absolute; top: 262px; height: 36px; padding: 0 9px; background: var(--label-bg); color: var(--white); font-size: 24px; line-height: 36px; }
  .label-before { left: 112px; }
  .label-after { left: 439px; width: 112px; text-align: center; }
  .pointers { position: absolute; inset: 0; }
</style>
</head>
<body>

<section class="card card-front" aria-label="Business card front">
  <div class="faint-block" aria-hidden="true"></div>
  <h1 class="holder-name">ADRIAN MERCER</h1>
  <p class="holder-role">Managing Director</p>
  <p class="address">4120 North Harlow Lane<br>Linden, MD 21900</p>
  <ul class="contact-list">
    <li><svg viewBox="0 0 16 16" aria-hidden="true"><path d="M3 2h3l1 3-2 1.5a9 9 0 0 0 4.5 4.5L11 9l3 1v3a1 1 0 0 1-1 1A12 12 0 0 1 2 3a1 1 0 0 1 1-1z"/></svg>+ 000 000 0000</li>
    <li><svg viewBox="0 0 16 16" aria-hidden="true"><path d="M1 3h14v10H1z M2 4l6 5 6-5" fill="none" stroke="#1a73b8" stroke-width="1.6"/></svg>info@crestlinesurface.com</li>
    <li><svg viewBox="0 0 16 16" aria-hidden="true"><circle cx="8" cy="8" r="6.5" fill="none" stroke="#1a73b8" stroke-width="1.6"/><path d="M1.5 8h13M8 1.5c-3 3.5-3 9.5 0 13M8 1.5c3 3.5 3 9.5 0 13" fill="none" stroke="#1a73b8" stroke-width="1.2"/></svg>www.crestlinesurface.com</li>
  </ul>
  <div class="social">
    <span class="social-dot" aria-hidden="true"></span>
    <span class="social-dot" aria-hidden="true"></span>
    <span class="social-dot" aria-hidden="true"></span>
    <span class="social-handle">@crestlinesurfacefin</span>
  </div>
  <div class="brand-lockup brand-front">
    <div class="brand-mark" aria-hidden="true"></div>
    <div class="brand-name"><span class="line-1">CRESTLINE</span><span class="line-2">SURFACE</span><span class="line-3">FINISHES</span></div>
  </div>
</section>

<section class="card card-back" aria-label="Business card back">
  <div class="surface-photo" role="img" aria-label="Before and after photo of a house driveway: cracked grey concrete on the left, stamped brown stone-pattern coating on the right"></div>
  <div class="brand-lockup brand-back">
    <div class="brand-mark" aria-hidden="true"></div>
    <div class="brand-name"><span class="line-1">CRESTLINE</span><span class="line-2">SURFACE</span><span class="line-3">FINISHES</span></div>
  </div>
  <svg class="pointers" viewBox="0 0 666 397" aria-hidden="true">
    <line x1="114" y1="298" x2="76" y2="345" stroke="#222" stroke-width="1.2"/>
    <circle cx="76" cy="345" r="4.5" fill="#222"/>
    <line x1="551" y1="298" x2="586" y2="345" stroke="#222" stroke-width="1.2"/>
    <circle cx="586" cy="345" r="4.5" fill="#222"/>
  </svg>
  <span class="compare-label label-before">BEFORE</span>
  <span class="compare-label label-after">AFTER</span>
</section>

</body>
</html>
```